Savings/Retirement Infographic

I need an infographic to convey the importance of retirement planning and saving regularly. It must be an attractive and compelling design that people want to read.

The design will primarily be used as a poster, but also as an emailer and a shorter version for an A5 flyer.

Content:

There are only two types of retirement funds
Big or Small

Big retirement funds = Foreign Travel,
Sailing,
Concerts,
Sky Diving,
Fishing,
Golf,
Fine Dining,
Spoiling Grandchildren,
Sandy Beaches.

Small retirement funds = Counting every penny,
Sitting at home,
Relying on family, friends and charity,
Turning off the heating in Winter

Big pensions are acquired over the length of a career with careful planning and motivation.

Small pensions take no effort at all.

Which are you aiming for?

Did you know?
1 in 5 people retiring in 2013 will be below the poverty line?
In the UK, 14% will rely solely on a state pension. That's less than AED 640 per week.
(Source: Calverley Cohort Study 2013)

Of 100 people aged 25 today, by age 65
1 will be wealthy
4 will be financially independent
5 will still be working
12 will be bankrupt
29 will already be dead
49 will be dependent on others

Of those still living, 86% will rely on friends, relatives and charity.

To retire on $30,000 per annum, you'll need approx.. $600,000 in today's terms.
That's $1,456,380 in 30 years with 3% inflation.
By saving in a bank earning ZERO interest, you need to save $4,045 each month for 30 years
If you invest in the markets and earn 5% interest each year, you only need to save $2,307 each month.
If you manage to get 10% per annum interest, you'll only need to save $934 per month. That's less than AED 3,450.

Please add a bar across the bottom with my contact details, leaving space for my photo and logo. Contact details:

E: rmorton@brisklane.com
M: 050 8126 473

```html
<!DOCTYPE html>
<html lang="en">
<head>
<meta charset="utf-8">
<title>There are only two types of retirement funds</title>
<link href="https://fonts.googleapis.com/css2?family=Arimo:wght@400;700&display=swap" rel="stylesheet">
<style>
:root{
  --bg-top:#24535f;
  --bg-bottom:#0d2a33;
  --band:#2b7f8d;
  --band-dark:#0f5563;
  --white:#ffffff;
  --red:#d9362b;
  --yellow:#f2c418;
  --blue:#4aa6dc;
  --orange:#e8882a;
  --grey:#a6a8a7;
  --lime:#c3cd22;
  --unit:#c9dde2;
  --unit-dead:#6f8e96;
  --tile-grey:#8c9ea6;
}
*{margin:0;padding:0;box-sizing:border-box}
html,body{width:849px;height:1200px;overflow:hidden}
body{font-family:"Arimo",Arial,sans-serif;color:var(--white);
  background:linear-gradient(180deg,var(--bg-top),var(--bg-bottom));position:relative}
.abs{position:absolute}
.title{left:0;width:849px;top:20px;text-align:center;font-size:29px;font-weight:700}
.rule{left:22px;width:806px;top:62px;height:2px;background:rgba(255,255,255,.35)}
.fund-band{top:72px;height:118px;background:var(--band)}
.fund-big{left:22px;width:545px}
.fund-small{left:575px;width:253px}
.bags{left:20px;top:14px;width:150px;height:86px;border-radius:10px;background:rgba(10,60,70,.45)}
.bag-small{left:12px;top:18px;width:48px;height:70px;border-radius:10px;background:rgba(10,60,70,.45)}
.fund-head{font-size:38px;font-weight:700;text-align:center}
.fund-text{font-size:17px;font-weight:700;text-align:center;line-height:1.2}
.tile{width:77px;height:77px;border-radius:8px}
.tile-label{width:100px;text-align:center;font-size:14px;font-weight:700;line-height:1.15}
.did-band{left:0;width:849px;top:485px;height:88px;background:var(--band-dark)}
.did-box{left:22px;top:8px;width:86px;height:72px;background:var(--band);border-radius:4px;
  font-size:22px;font-weight:700;line-height:1.05;padding:6px 8px}
.did-text{font-size:19px;font-weight:700;line-height:1.2}
.source{right:22px;top:596px;font-size:14px;font-weight:700}
.of100{left:552px;top:628px;font-size:40px;font-weight:700;line-height:1}
.of100 small{display:block;font-size:21px;margin-top:4px}
.outcomes{left:552px;top:700px;font-size:16px;font-weight:700;line-height:20px;list-style:none}
.living{left:22px;width:806px;top:826px;height:32px;background:var(--band);text-align:center;
  font-size:16px;font-weight:700;line-height:32px}
.plan-head{left:235px;width:403px;top:888px;height:38px;background:var(--band-dark);
  text-align:center;font-size:24px;font-weight:700;line-height:40px}
.plan{font-size:16px;font-weight:700;line-height:1.22;text-align:center;display:flex;align-items:center;justify-content:center;padding:0 12px}
.brand{left:372px;top:1104px;display:flex;align-items:center;gap:8px}
.brand-mark{width:34px;height:34px;background:var(--band)}
.brand-name{font-size:20px;font-weight:700}
.contact{left:0;width:849px;top:1160px;height:40px;background:var(--band-dark);text-align:center;
  font-size:22px;font-weight:700;line-height:40px}
</style>
</head>
<body>
<h1 class="abs title">There are only two types of retirement funds</h1>
<div class="abs rule"></div>

<section class="abs fund-band fund-big">
  <div class="abs bags" role="img" aria-label="Three money bags with dollar signs"></div>
  <div class="abs fund-head" style="left:190px;width:340px;top:6px">Big</div>
  <p class="abs fund-text" style="left:190px;width:340px;top:54px">pensions are acquired over the length of a career with careful planning and motivation.</p>
</section>
<section class="abs fund-band fund-small">
  <div class="abs bag-small" role="img" aria-label="One small money bag with a dollar sign"></div>
  <div class="abs fund-head" style="left:70px;width:175px;top:6px">Small</div>
  <p class="abs fund-text" style="left:70px;width:175px;top:54px">pensions take no effort at all.</p>
</section>

<div class="abs tile" style="left:77px;top:206px;background:#3b8fa0" role="img" aria-label="Sailing boat icon"></div>
<div class="abs tile" style="left:180px;top:206px;background:#8e3a8a" role="img" aria-label="Music notes icon"></div>
<div class="abs tile" style="left:283px;top:206px;background:#2e8fcf" role="img" aria-label="Sky diver icon"></div>
<div class="abs tile" style="left:386px;top:206px;background:#2c6fb5" role="img" aria-label="Fish icon"></div>
<div class="abs tile" style="left:587px;top:206px;background:var(--tile-grey)" role="img" aria-label="Piggy bank icon"></div>
<div class="abs tile" style="left:690px;top:206px;background:var(--tile-grey)" role="img" aria-label="Armchair icon"></div>
<div class="abs tile-label" style="left:65px;top:292px">Sailing</div>
<div class="abs tile-label" style="left:168px;top:292px">Concerts</div>
<div class="abs tile-label" style="left:271px;top:292px">Sky<br>Diving</div>
<div class="abs tile-label" style="left:374px;top:292px">Fishing</div>
<div class="abs tile-label" style="left:575px;top:292px">Counting<br>every penny</div>
<div class="abs tile-label" style="left:678px;top:292px">Sitting at<br>home</div>

<div class="abs tile" style="left:77px;top:338px;background:var(--orange)" role="img" aria-label="Golfer icon"></div>
<div class="abs tile" style="left:180px;top:338px;background:#4caf50" role="img" aria-label="Plate and cutlery icon"></div>
<div class="abs tile" style="left:283px;top:338px;background:var(--red)" role="img" aria-label="Gift box icon"></div>
<div class="abs tile" style="left:386px;top:338px;background:var(--yellow)" role="img" aria-label="Swimmer icon"></div>
<div class="abs tile" style="left:587px;top:338px;background:var(--tile-grey)" role="img" aria-label="Group of people icon"></div>
<div class="abs tile" style="left:690px;top:338px;background:var(--tile-grey)" role="img" aria-label="Thermometer icon"></div>
<div class="abs tile-label" style="left:65px;top:424px">Golf</div>
<div class="abs tile-label" style="left:168px;top:424px">Fine<br>Dining</div>
<div class="abs tile-label" style="left:271px;top:424px">Spoiling<br>Grand-<br>children</div>
<div class="abs tile-label" style="left:374px;top:424px">Sandy<br>Beaches</div>
<div class="abs tile-label" style="left:575px;top:424px">Relying on<br>family, friends<br>and charity</div>
<div class="abs tile-label" style="left:678px;top:424px">Turning off<br>the heating<br>in Winter</div>

<section class="abs did-band">
  <div class="abs did-box">Did<br>you<br>know?</div>
  <svg class="abs" style="left:118px;top:20px" width="92" height="48" viewBox="0 0 92 48">
    <rect x="0" y="0" width="14" height="48" rx="7" fill="#d9362b"/>
    <rect x="19" y="0" width="14" height="48" rx="7" fill="#ffffff"/>
    <rect x="38" y="0" width="14" height="48" rx="7" fill="#ffffff"/>
    <rect x="57" y="0" width="14" height="48" rx="7" fill="#ffffff"/>
    <rect x="76" y="0" width="14" height="48" rx="7" fill="#ffffff"/>
  </svg>
  <p class="abs did-text" style="left:220px;top:18px;width:230px">1 in 5 people retiring in 2013 will be below the poverty line?</p>
  <svg class="abs" style="left:462px;top:12px" width="62" height="62" viewBox="0 0 62 62">
    <circle cx="31" cy="31" r="29" fill="#ffffff"/>
    <path d="M31 31 L31 2 A29 29 0 0 1 54.4 13.9 Z" fill="#d9362b"/>
    <circle cx="31" cy="31" r="29" fill="none" stroke="#d9362b" stroke-width="3"/>
  </svg>
  <p class="abs did-text" style="left:536px;top:8px;width:300px">In the UK, 14% will rely solely on a state pension. That's less than AED 640 per week.</p>
</section>
<p class="abs source">(Source: Calverley Cohort Study 2013)</p>

<svg class="abs" style="left:22px;top:632px" width="520" height="142" viewBox="0 0 520 142" role="img" aria-label="Chart of 100 people by outcome at age 65">
  <defs>
    <pattern id="unit-living" width="20.8" height="36" patternUnits="userSpaceOnUse">
      <rect x="4" y="2" width="12" height="31" rx="6" fill="#c9dde2"/>
    </pattern>
    <pattern id="unit-dead" width="20.8" height="36" patternUnits="userSpaceOnUse">
      <rect x="4" y="2" width="12" height="31" rx="6" fill="#6f8e96"/>
    </pattern>
  </defs>
  <g>
    <rect x="4" y="2" width="12" height="31" rx="6" fill="#d9362b"/>
    <rect x="24.8" y="2" width="12" height="31" rx="6" fill="#f2c418"/>
    <rect x="45.6" y="2" width="12" height="31" rx="6" fill="#f2c418"/>
    <rect x="66.4" y="2" width="12" height="31" rx="6" fill="#f2c418"/>
    <rect x="87.2" y="2" width="12" height="31" rx="6" fill="#f2c418"/>
    <rect x="108" y="2" width="12" height="31" rx="6" fill="#4aa6dc"/>
    <rect x="128.8" y="2" width="12" height="31" rx="6" fill="#4aa6dc"/>
    <rect x="149.6" y="2" width="12" height="31" rx="6" fill="#4aa6dc"/>
    <rect x="170.4" y="2" width="12" height="31" rx="6" fill="#4aa6dc"/>
    <rect x="191.2" y="2" width="12" height="31" rx="6" fill="#4aa6dc"/>
    <rect x="212" y="2" width="12" height="31" rx="6" fill="#e8882a"/>
    <rect x="232.8" y="2" width="12" height="31" rx="6" fill="#e8882a"/>
    <rect x="253.6" y="2" width="12" height="31" rx="6" fill="#e8882a"/>
    <rect x="274.4" y="2" width="12" height="31" rx="6" fill="#e8882a"/>
    <rect x="295.2" y="2" width="12" height="31" rx="6" fill="#e8882a"/>
    <rect x="316" y="2" width="12" height="31" rx="6" fill="#e8882a"/>
    <rect x="336.8" y="2" width="12" height="31" rx="6" fill="#e8882a"/>
    <rect x="357.6" y="2" width="12" height="31" rx="6" fill="#e8882a"/>
    <rect x="378.4" y="2" width="12" height="31" rx="6" fill="#e8882a"/>
    <rect x="399.2" y="2" width="12" height="31" rx="6" fill="#e8882a"/>
    <rect x="420" y="2" width="12" height="31" rx="6" fill="#e8882a"/>
    <rect x="440.8" y="2" width="12" height="31" rx="6" fill="#e8882a"/>
  </g>
  <rect x="457.6" y="0" width="62.4" height="36" fill="url(#unit-dead)"/>
  <rect x="0" y="36" width="520" height="36" fill="url(#unit-dead)"/>
  <rect x="0" y="72" width="20.8" height="36" fill="url(#unit-dead)"/>
  <rect x="20.8" y="72" width="499.2" height="36" fill="url(#unit-living)"/>
  <rect x="0" y="108" width="520" height="36" fill="url(#unit-living)"/>
</svg>

<h2 class="abs of100">Of 100 people<small>aged 25 today, by age 65</small></h2>
<ul class="abs outcomes">
  <li>1 will be wealthy</li>
  <li>4 will be financially independent</li>
  <li>5 will still be working</li>
  <li>12 will be bankrupt</li>
  <li>29 will already be dead</li>
  <li>49 will be dependent on others</li>
</ul>
<p class="abs living">Of those still living, 86% will rely on friends, relatives and charity.</p>

<div class="abs plan-head">FINANCIAL PLAN</div>
<div class="abs plan" style="left:22px;width:210px;top:888px;height:192px;background:var(--blue)">To retire on $30,000 per annum, you'll need approx. $600,000 in today's terms. That's $1,456,380 in 30 years with 3% inflation.</div>
<div class="abs plan" style="left:235px;width:208px;top:926px;height:134px;background:var(--grey)">By saving in a bank earning ZERO interest, you need to save $4,045 each month for 30 years.</div>
<div class="abs plan" style="left:446px;width:192px;top:926px;height:134px;background:var(--orange)">If you invest in the markets and earn 5% interest each year, you only need to save $2,307 each month.</div>
<div class="abs plan" style="left:641px;width:187px;top:888px;height:192px;background:var(--lime)">If you manage to get 10% per annum interest, you'll only need to save $934 per month. That's less than AED 3,450.</div>

<div class="abs brand"><span class="brand-mark"></span><span class="brand-name">Brisklane</span></div>
<footer class="abs contact">E: rmorton@brisklane.com, M: 050 8126 473</footer>
</body>
</html>
```